Torvel, Inc. new buisness cards - brand guide included

We need new business cards. SLEAK SIMPLE FINANCE. They must include a place for NAME, TITLE, CELL, OFFICE PHONE, EMAIL. they also must include our services across the bottom. AIR, OCEAN, FTL, LTL, EXPRESS. for reference this will be being handed to some of the most prestigious shipping companies in a america.

Target Market(s)

Finance and corporate

Contact Information for Business Card

We need new business cards. SLEAK SIMPLE FINANCE. They must include a place for NAME, TITLE, CELL, OFFICE PHONE, EMAIL. they also must include our services across the bottom. AIR, OCEAN, FTL, LTL, EXPRESS.

Requirements
Must have
• We need new business cards. SLEAK SIMPLE FINANCE. They must include a place for NAME, TITLE, CELL, OFFICE PHONE, EMAIL. they also must include our services across the bottom. AIR, OCEAN, FTL, LTL, EXPRESS.
Nice to have
• USE THE COLORS AND LOGO IN THE BRAND GUIDE :)

```html
<!DOCTYPE html>
<html lang="en">
<head>
<meta charset="utf-8">
<title>Torvel, Inc. Business Cards</title>
<link href="https://fonts.googleapis.com/css2?family=Montserrat:wght@400;500&family=Libre+Baskerville:wght@700&display=swap" rel="stylesheet">
<style>
  :root {
    --backdrop: #141414;
    --card: #1f1f1f;
    --ink: #f2efe6;
    --rule: #bdbab2;
  }
  * { margin: 0; padding: 0; box-sizing: border-box; }
  html, body { width: 1200px; height: 900px; overflow: hidden; background: var(--backdrop); }
  .canvas { position: relative; width: 1200px; height: 900px; }
  .card {
    position: absolute; left: 260px; width: 680px; height: 388px;
    background: var(--card); border-radius: 18px; color: var(--ink);
    font-family: "Montserrat", sans-serif;
  }
  .card--front { top: 34px; }
  .card--back { top: 470px; }

  .wordmark {
    position: absolute; left: 0; right: 0; text-align: center;
    font-family: "Montserrat", sans-serif; font-weight: 500;
    letter-spacing: 0.22em; color: var(--ink);
  }
  .card--front .wordmark { top: 128px; font-size: 54px; }
  .card--back .wordmark { top: 48px; font-size: 44px; }

  .services {
    position: absolute; top: 290px; left: 0; right: 0; text-align: center;
    font-size: 17px; letter-spacing: 0.08em;
  }
  .services .dot { margin: 0 8px; }

  .identity { position: absolute; top: 168px; left: 150px; width: 260px; text-align: center; }
  .identity__name {
    font-family: "Libre Baskerville", serif; font-weight: 700;
    font-size: 24px; letter-spacing: 0.04em; text-transform: uppercase;
  }
  .identity__title { margin-top: 6px; font-size: 17px; letter-spacing: 0.04em; }

  .rule { position: absolute; height: 1px; background: var(--rule); }
  .rule--address { top: 160px; left: 430px; width: 210px; }
  .rule--contact { top: 252px; left: 40px; width: 250px; }

  .address {
    position: absolute; top: 176px; right: 40px; text-align: right;
    font-size: 16px; line-height: 1.6; letter-spacing: 0.02em;
  }
  .contact { position: absolute; top: 266px; left: 40px; list-style: none;
    font-size: 17px; line-height: 1.75; letter-spacing: 0.03em; }
  .contact li, .address .web { display: flex; align-items: center; gap: 10px; }
  .address .web { justify-content: flex-end; }
  .icon { width: 16px; height: 16px; fill: none; stroke: var(--ink); stroke-width: 1.6; flex: none; }
</style>
</head>
<body>
<main class="canvas">

  <section class="card card--front" aria-label="Card front">
    <div class="wordmark">TORVEL</div>
    <p class="services">Air<span class="dot">•</span>Ocean<span class="dot">•</span>Ftl<span class="dot">•</span>Ltl<span class="dot">•</span>Express</p>
  </section>

  <section class="card card--back" aria-label="Card back">
    <div class="wordmark">TORVEL</div>

    <div class="rule rule--address"></div>
    <div class="identity">
      <p class="identity__name">Delan Marsh</p>
      <p class="identity__title">Founder/CEO</p>
    </div>

    <div class="address">
      <p>48 B. Harlow Lane</p>
      <p>Country Name, AB 4120</p>
      <p class="web">
        <svg class="icon" viewBox="0 0 16 16" aria-hidden="true"><circle cx="8" cy="8" r="6.5"/><ellipse cx="8" cy="8" rx="2.8" ry="6.5"/><line x1="1.5" y1="8" x2="14.5" y2="8"/></svg>
        www.torvelinc.com
      </p>
    </div>

    <div class="rule rule--contact"></div>
    <ul class="contact">
      <li>
        <svg class="icon" viewBox="0 0 16 16" aria-hidden="true"><rect x="4" y="1.5" width="8" height="13" rx="1.5"/><line x1="7" y1="12.3" x2="9" y2="12.3"/></svg>
        555.014.2281
      </li>
      <li>
        <svg class="icon" viewBox="0 0 16 16" aria-hidden="true"><path d="M3 2.5l2.5-.5 1.5 3.2-1.6 1.2a8 8 0 0 0 3.7 3.7l1.2-1.6 3.2 1.5-.5 2.5c-6 .5-10.5-4-10-10z"/></svg>
        555.014.7730
      </li>
      <li>
        <svg class="icon" viewBox="0 0 16 16" aria-hidden="true"><rect x="1.5" y="3.5" width="13" height="9"/><path d="M1.5 3.5L8 9l6.5-5.5"/></svg>
        info@torvelinc.com
      </li>
    </ul>
  </section>

</main>
</body>
</html>
```